Medical Device Company needs website

We are a start-up medical device company looking to sell boot (foot) and brace (ankle) products on Shopify. We are still working on the name but you can use Kaltir as a placeholder- no logo yet)

Website information:
- Look: modern/tech with clean lines and symmetry.
- Colors: teal, white, black, and greys.
- Headers: home, shop, about us, help, blog
- Icons (upper right): search, my account and shopping cart
-place to sign up for newsletter

```html
<!DOCTYPE html>
<html lang="en">
<head>
<meta charset="utf-8">
<title>Kaltir — Boots &amp; Ankles</title>
<link href="https://fonts.googleapis.com/css2?family=Jost:wght@400;500;600&display=swap" rel="stylesheet">
<style>
  :root {
    --teal: #0f8a8c;
    --ink: #111111;
    --white: #ffffff;
    --mist: #f4f4f4;
    --line: #e2e2e2;
  }
  * { box-sizing: border-box; margin: 0; padding: 0; }
  html, body { width: 1200px; height: 1200px; overflow: hidden; background: var(--mist); font-family: 'Jost', sans-serif; color: var(--ink); }
  .page { position: relative; width: 1200px; height: 1200px; }
  .topbar { position: absolute; top: 0; left: 0; width: 1200px; height: 22px; background: var(--mist); }
  .header { position: absolute; top: 22px; left: 0; width: 1200px; height: 56px; background: var(--white); border-bottom: 1px solid var(--line); }
  .nav { position: absolute; top: 0; left: 160px; height: 56px; display: flex; align-items: center; gap: 0; }
  .nav a { position: absolute; font-size: 10.5px; font-weight: 500; color: var(--ink); text-decoration: none; white-space: nowrap; top: 22px; }
  .brand { position: absolute; left: 0; width: 1200px; top: 12px; display: flex; justify-content: center; align-items: center; gap: 7px; }
  .brand-mark { width: 16px; height: 16px; background: var(--teal); border-radius: 3px; }
  .brand-name { font-size: 24px; font-weight: 600; letter-spacing: 1.5px; color: var(--ink); text-transform: uppercase; }
  .icons { position: absolute; top: 19px; left: 947px; display: flex; gap: 8px; }
  .icons svg { width: 18px; height: 18px; }
  .hero { position: absolute; top: 78px; left: 0; width: 1200px; height: 711px; overflow: hidden; }
  .hero-photo { position: absolute; inset: 0; background: linear-gradient(100deg, #0f4f80 0%, #1b4a6c 28%, #3b4a57 45%, #5d646b 70%, #6a7078 100%); }
  .hero-shade { position: absolute; inset: 0; background: linear-gradient(180deg, rgba(0,0,0,0.05), rgba(10,20,35,0.25)); }
  .hero-copy { position: absolute; left: 0; width: 1200px; text-align: center; color: var(--white); }
  .eyebrow { position: absolute; top: 270px; left: 0; width: 1200px; text-align: center; font-size: 11.5px; font-weight: 500; letter-spacing: 3px; color: var(--white); }
  .hero-title { position: absolute; top: 370px; left: 0; width: 1200px; text-align: center; font-size: 51px; font-weight: 500; color: var(--white); line-height: 1; transform: translateY(-70px); }
  .hero-sub { position: absolute; top: 364px; left: 0; width: 1200px; text-align: center; font-size: 13px; font-weight: 500; color: var(--white); }
  .btn { position: absolute; border: 1px solid var(--white); color: var(--white); font-size: 9px; font-weight: 500; letter-spacing: 1.5px; display: flex; align-items: center; justify-content: center; text-decoration: none; }
  .hero .btn { left: 549px; top: 412px; width: 102px; height: 29px; }
  .dots { position: absolute; top: 672px; left: 592px; display: flex; gap: 7px; }
  .dot { width: 8px; height: 8px; border-radius: 50%; border: 1.2px solid var(--teal); }
  .dot.active { background: var(--teal); }
  .tile { position: absolute; top: 792px; width: 594px; height: 352px; overflow: hidden; }
  .tile.boots { left: 3px; }
  .tile.ankles { left: 603px; }
  .tile-photo { position: absolute; inset: 0; }
  .boots .tile-photo { background: linear-gradient(170deg, #3c4a32 0%, #4d4334 35%, #5a4231 55%, #3a3a38 100%); }
  .ankles .tile-photo { background: linear-gradient(100deg, #154f78 0%, #2c4b63 35%, #5a626a 65%, #6b7179 100%); }
  .tile-title { position: absolute; top: 240px; left: 0; width: 594px; text-align: center; font-size: 32px; font-weight: 500; color: var(--white); letter-spacing: 0.5px; }
  .tile .btn { top: 292px; width: 85px; height: 28px; left: 255px; font-size: 8.5px; letter-spacing: 1px; border-width: 1.5px; }
  .footer-band { position: absolute; top: 1144px; left: 0; width: 1200px; height: 25px; background: var(--white); }
</style>
</head>
<body>
<div class="page">
  <div class="topbar"></div>

  <header class="header">
    <nav class="nav">
      <a href="#" style="left:0">Home</a>
      <a href="#" style="left:59px">Shop</a>
      <a href="#" style="left:115px">About Us</a>
      <a href="#" style="left:189px">Blog</a>
      <a href="#" style="left:242px">Help</a>
    </nav>
    <div class="brand">
      <span class="brand-mark"></span>
      <span class="brand-name">Kaltir</span>
    </div>
    <div class="icons">
      <svg viewBox="0 0 24 24" fill="none" stroke="#111" stroke-width="2"><circle cx="10.5" cy="10.5" r="7"/><line x1="15.5" y1="15.5" x2="21" y2="21"/></svg>
      <svg viewBox="0 0 24 24" fill="none" stroke="#111" stroke-width="2"><circle cx="12" cy="8" r="4.5"/><path d="M3.5 21.5c0-5 4-7.5 8.5-7.5s8.5 2.5 8.5 7.5z"/></svg>
      <svg viewBox="0 0 24 24" fill="none" stroke="#111" stroke-width="2"><path d="M12 20.5 4 12.6A4.8 4.8 0 0 1 12 6.4a4.8 4.8 0 0 1 8 6.2z"/></svg>
      <svg viewBox="0 0 24 24" fill="none" stroke="#111" stroke-width="2"><rect x="5" y="6.5" width="14" height="15"/><path d="M9 6.5V4h6v2.5"/></svg>
    </div>
  </header>

  <section class="hero">
    <div class="hero-photo" role="img" aria-label="Clinician in a white coat examining a patient's foot in a blue treatment room"></div>
    <div class="hero-shade"></div>
    <p class="eyebrow">Sale</p>
    <h1 class="hero-title">Trending Products</h1>
    <p class="hero-sub">Best ever medical products</p>
    <a href="#" class="btn">Shop Now</a>
    <div class="dots"><span class="dot active"></span><span class="dot"></span></div>
  </section>

  <section class="tile boots">
    <div class="tile-photo" role="img" aria-label="Child wearing rubber boots standing on a leafy park path"></div>
    <h2 class="tile-title">BOOT PRODUCTS</h2>
    <a href="#" class="btn">Shop Now</a>
  </section>

  <section class="tile ankles">
    <div class="tile-photo" role="img" aria-label="Clinician supporting a patient's ankle in a treatment room"></div>
    <h2 class="tile-title">ANKLE PRODUCTS</h2>
    <a href="#" class="btn">Shop Now</a>
  </section>

  <div class="footer-band"></div>
</div>
</body>
</html>
```